Business Card Design for Engineering Firm

Need a business card design for small mechanical and plumbing engineering form based in Utah. Design should be customizable for all employees.

```html
<!DOCTYPE html>
<html lang="en">
<head>
<meta charset="utf-8">
<title>Larkspur Engineering – Business Card</title>
<link rel="stylesheet" href="https://fonts.googleapis.com/css2?family=Montserrat:wght@400;500;700&display=swap">
<style>
  :root {
    --stage: #2e2e2e;
    --card-dark: #0b0b0b;
    --card-light: #ffffff;
    --brand-red: #8c1a12;
    --ink-grey: #3a3a3a;
    --soft-grey: #6e6e6e;
  }
  * { margin: 0; padding: 0; box-sizing: border-box; }
  html, body {
    width: 1200px; height: 1186px; overflow: hidden;
    background: var(--stage);
    font-family: "Montserrat", sans-serif;
  }
  .sheet {
    position: relative; width: 1200px; height: 1186px;
    display: flex; flex-direction: column; align-items: center;
    gap: 58px; padding-top: 50px;
  }
  .card {
    position: relative; width: 900px; height: 514px;
    border-radius: 28px; overflow: hidden;
  }
  .card--back { background: var(--card-dark); }
  .card--front { background: var(--card-light); }

  /* wordmark */
  .wordmark { display: flex; align-items: center; gap: 16px; color: var(--brand-red); font-weight: 700; }
  .wordmark__square { width: 22px; height: 22px; background: var(--brand-red); flex: none; }
  .wordmark__text { display: flex; flex-direction: column; line-height: 1; }
  .wordmark__main { letter-spacing: 1px; }
  .wordmark__sub { letter-spacing: 9px; }

  .card--back .wordmark {
    position: absolute; left: 50%; top: 50%; transform: translate(-50%, -50%);
  }
  .card--back .wordmark__main { font-size: 58px; }
  .card--back .wordmark__sub { font-size: 22px; margin-top: 8px; letter-spacing: 13px; }
  .card--back .wordmark__square { width: 34px; height: 34px; }

  .card--front .wordmark { position: absolute; left: 70px; top: 170px; }
  .card--front .wordmark__main { font-size: 38px; }
  .card--front .wordmark__sub { font-size: 15px; margin-top: 6px; }

  .divider {
    position: absolute; left: 70px; right: 40px; top: 272px;
    height: 2px; background: var(--brand-red);
  }

  .person { position: absolute; left: 70px; top: 292px; }
  .person__name { font-size: 30px; font-weight: 700; color: var(--brand-red); }
  .person__role { font-size: 18px; font-weight: 400; color: var(--ink-grey); margin-top: 2px; }

  .contacts { position: absolute; left: 70px; top: 372px; list-style: none; }
  .contacts__item {
    display: flex; align-items: center; gap: 14px;
    font-size: 17px; color: var(--ink-grey); height: 27px;
  }
  .contacts__icon { width: 16px; height: 16px; fill: var(--brand-red); flex: none; }

  .address {
    position: absolute; right: 50px; top: 294px; text-align: right;
    font-size: 17px; line-height: 1.3; color: var(--ink-grey); font-style: normal;
  }
</style>
</head>
<body>
<main class="sheet">
  <section class="card card--back" aria-label="Card back">
    <div class="wordmark">
      <span class="wordmark__square"></span>
      <span class="wordmark__text">
        <span class="wordmark__main">LARKSPUR</span>
        <span class="wordmark__sub">ENGINEERING</span>
      </span>
    </div>
  </section>

  <section class="card card--front" aria-label="Card front">
    <div class="wordmark">
      <span class="wordmark__square"></span>
      <span class="wordmark__text">
        <span class="wordmark__main">LARKSPUR</span>
        <span class="wordmark__sub">ENGINEERING</span>
      </span>
    </div>

    <div class="divider"></div>

    <div class="person">
      <p class="person__name">Daniel Hartley</p>
      <p class="person__role">Owner</p>
    </div>

    <ul class="contacts">
      <li class="contacts__item">
        <svg class="contacts__icon" viewBox="0 0 16 16"><path d="M2 5c0-2 2-3 6-3s6 1 6 3v1h-3V4.5H5V6H2z M3 7h10l1 7H2z"/></svg>
        +49 404 555 0182
      </li>
      <li class="contacts__item">
        <svg class="contacts__icon" viewBox="0 0 16 16"><path d="M4 1h8v14H4z M5.5 3v9h5V3z"/></svg>
        +49 404 555 0182
      </li>
      <li class="contacts__item">
        <svg class="contacts__icon" viewBox="0 0 16 16"><path d="M1 3h14v10H1z M2 4l6 5 6-5v-0.2H2z" fill-rule="evenodd"/></svg>
        info@larkspur-eng.com
      </li>
      <li class="contacts__item">
        <svg class="contacts__icon" viewBox="0 0 16 16"><circle cx="8" cy="8" r="7"/><path d="M1 8h14M8 1c-3 3.5-3 10.5 0 14M8 1c3 3.5 3 10.5 0 14" stroke="#fff" stroke-width="1" fill="none"/></svg>
        www.larkspur-eng.com
      </li>
    </ul>

    <address class="address">Lindenweg 42<br>22769 Hamburg</address>
  </section>
</main>
</body>
</html>
```